The Quillmore Daily Ledger

I am making a journal for tracking pain symptoms for TMJ (Jaw) pain. I have the cover designed and I just need the journal page designed that will repeat throughout the journal. The journal is the image on the left of the bundle. The page I would like to be developed is the picture that I hand sketched out. It should be a 6 x 9 page, similar to the attached example. Greyscale, no color. Thank you!

Target Market(s)

20-55 year old women

Industry/Entity Type

Healthcare

Colors

Designer to choose only greyscale colors for use in the design.

Requirements
Must have
• A neat, well-designed page with the content I have sketched out by hand.
Nice to have
• Creative display of the content I provided and development of the pain scale and pain diagram faces in a professional looking way.

```html
<!DOCTYPE html>
<html lang="en">
<head>
<meta charset="utf-8">
<title>The Quillmore Daily Ledger – Daily Journal Page</title>
<link href="https://fonts.googleapis.com/css2?family=Montserrat:wght@400;500;700&display=swap" rel="stylesheet">
<style>
  :root {
    --ink: #111111;
    --ink-soft: #555555;
    --rule-faint: #c4c4c4;
    --face-light: #d9d9d9;
    --face-dark: #8a8a8a;
    --paper: #ffffff;
    --backdrop: #ececec;
  }
  * { box-sizing: border-box; margin: 0; padding: 0; }
  html, body { width: 1200px; height: 764px; overflow: hidden; }
  body { background: var(--backdrop); font-family: 'Montserrat', sans-serif; color: var(--ink); }

  .journal-page {
    position: absolute; left: 346px; top: 24px; width: 507px; height: 716px;
    background: var(--paper); box-shadow: 0 2px 8px rgba(0,0,0,.18);
  }
  .journal-page > * { position: absolute; }

  .brand { left: 0; right: 0; top: 20px; display: flex; justify-content: center; align-items: center; gap: 8px; }
  .brand-dot { width: 30px; height: 30px; border: 2.5px solid var(--ink); border-radius: 50%; }
  .brand-name { font-weight: 700; font-size: 15px; line-height: 1.05; width: 120px; }

  .date-bar {
    left: 17px; width: 473px; top: 76px; height: 21px; border: 1.2px solid var(--ink); border-radius: 11px;
    font-weight: 700; font-size: 9px; display: flex; align-items: center; padding-left: 16px;
  }
  .date-bar .day-label { position: absolute; left: 258px; }

  .time-table { top: 112px; width: 200px; height: 76px; }
  .time-table.first { left: 22px; }
  .time-table.second { left: 285px; }
  .time-table .col-label { position: absolute; top: 2px; font-weight: 700; font-size: 9px; }
  .time-table svg { position: absolute; left: 0; top: 0; }
  .extra-box { left: 448px; top: 229px; display: flex; align-items: center; gap: 3px; font-size: 9px; }

  .section-title {
    left: 22px; right: 23px; font-weight: 700; font-size: 9.2px; letter-spacing: .1px;
    border-bottom: 1.2px solid var(--ink); padding-bottom: 3px;
  }
  .box { display: inline-block; width: 10px; height: 10px; border: 1px solid var(--ink); flex: none; }
  .box.small { width: 7px; height: 7px; }
  .option { display: flex; align-items: center; gap: 4px; font-size: 9.5px; white-space: nowrap; }
  .option.small { font-size: 6.5px; gap: 3px; }

  .pain-scale { left: 22px; top: 288px; display: flex; gap: 0; }
  .pain-scale.row { top: 288px; }
  .scale-row { left: 22px; top: 286px; display: flex; }
  .scale-row .option { width: 48.2px; }

  .face-chart { left: 22px; top: 350px; display: flex; }
  .face-cell { width: 47.5px; border-left: 1px solid var(--ink); display: flex; flex-direction: column; align-items: center; padding: 0 3px; height: 90px; }
  .face-cell:first-child { border-left: none; }
  .face-art { width: 40px; height: 48px; border-radius: 4px; background: linear-gradient(180deg, var(--face-light), var(--face-dark)); }
  .face-name { font-weight: 700; font-size: 5.5px; margin-top: 4px; }
  .face-note { font-size: 4.6px; text-align: center; line-height: 1.2; color: var(--ink-soft); }

  .mini-title { font-weight: 700; font-size: 7.5px; border-bottom: 1px solid var(--ink); padding-bottom: 1px; }
  .option-grid { display: grid; grid-template-columns: 97px auto; row-gap: 4px; margin-top: 5px; margin-bottom: 6px; }

  .trigger-grid { left: 22px; top: 472px; display: grid; grid-template-columns: 147px 94px 134px auto; row-gap: 7px; }
  .relief-grid { left: 23px; top: 612px; display: grid; grid-template-columns: 206px 155px auto; row-gap: 7px; }

  .state-line { display: flex; align-items: center; gap: 8px; border-bottom: 1.2px solid var(--ink); padding-bottom: 2px; }
  .state-line .label { font-weight: 700; font-size: 9px; margin-right: 4px; }

  .others-line { left: 257px; top: 679px; width: 207px; border-bottom: 1px solid var(--ink); }
  .notes-lines { left: 21px; right: 23px; top: 0; }
  .note-rule { left: 21px; right: 23px; border-bottom: 1px solid var(--ink); }
</style>
</head>
<body>
<main class="journal-page">

  <header class="brand">
    <span class="brand-dot"></span>
    <span class="brand-name">The Quillmore Daily Ledger</span>
  </header>

  <div class="date-bar"><span>DATE</span><span class="day-label">DAY OF THE WEEK</span></div>

  <div class="time-table first">
    <svg width="200" height="76">
      <line x1="0" y1="13" x2="198" y2="13" stroke="#111" stroke-width="1.2"/>
      <line x1="15" y1="0" x2="15" y2="76" stroke="#111" stroke-width="1.2"/>
      <line x1="0" y1="30" x2="200" y2="30" stroke="#c4c4c4" stroke-width=".7"/>
      <line x1="0" y1="45" x2="200" y2="45" stroke="#c4c4c4" stroke-width=".7"/>
      <line x1="0" y1="61" x2="200" y2="61" stroke="#c4c4c4" stroke-width=".7"/>
      <line x1="66" y1="14" x2="66" y2="76" stroke="#c4c4c4" stroke-width=".7"/>
      <line x1="117" y1="14" x2="117" y2="76" stroke="#c4c4c4" stroke-width=".7"/>
    </svg>
    <span class="col-label" style="left:21px">BEGIN</span>
    <span class="col-label" style="left:84px">END</span>
    <span class="col-label" style="left:131px">DURATION</span>
  </div>

  <div class="time-table second">
    <svg width="200" height="76">
      <line x1="0" y1="13" x2="198" y2="13" stroke="#111" stroke-width="1.2"/>
      <line x1="15" y1="0" x2="15" y2="76" stroke="#111" stroke-width="1.2"/>
      <line x1="0" y1="30" x2="200" y2="30" stroke="#c4c4c4" stroke-width=".7"/>
      <line x1="0" y1="45" x2="200" y2="45" stroke="#c4c4c4" stroke-width=".7"/>
      <line x1="0" y1="61" x2="200" y2="61" stroke="#c4c4c4" stroke-width=".7"/>
      <line x1="66" y1="14" x2="66" y2="76" stroke="#c4c4c4" stroke-width=".7"/>
      <line x1="117" y1="14" x2="117" y2="76" stroke="#c4c4c4" stroke-width=".7"/>
    </svg>
    <span class="col-label" style="left:21px">BEGIN</span>
    <span class="col-label" style="left:84px">END</span>
    <span class="col-label" style="left:131px">DURATION</span>
  </div>
  <div class="extra-box" style="top:224px;left:-1000px"></div>
  <div class="option" style="left:448px;top:227px;position:absolute"><span class="box"></span>10</div>

  <h2 class="section-title" style="top:267px">SEVERITY OF PAIN (CIRCLE RANGE)</h2>
  <div class="scale-row" style="top:288px">
    <span class="option"><span class="box"></span>1</span>
    <span class="option"><span class="box"></span>2</span>
    <span class="option"><span class="box"></span>3</span>
    <span class="option"><span class="box"></span>4</span>
    <span class="option"><span class="box"></span>5</span>
    <span class="option"><span class="box"></span>6</span>
    <span class="option"><span class="box"></span>7</span>
    <span class="option"><span class="box"></span>8</span>
    <span class="option"><span class="box"></span>9</span>
  </div>

  <h2 class="section-title" style="top:322px">LOCATION</h2>
  <div class="face-chart" style="top:349px">
    <div class="face-cell"><div class="face-art" role="img" aria-label="Head diagram shading temples and area in front of ears"></div><span class="face-name">TMJ</span><span class="face-note">pain is at temples, in front of ears.</span></div>
    <div class="face-cell"><div class="face-art" role="img" aria-label="Head diagram shading browbone and cheekbones"></div><span class="face-name">Sinus</span><span class="face-note">pain is behind browbone and/or cheekbone.</span></div>
    <div class="face-cell"><div class="face-art" role="img" aria-label="Head diagram shading area around one eye"></div><span class="face-name">Cluster</span><span class="face-note">pain is in and around one eye.</span></div>
    <div class="face-cell"><div class="face-art" role="img" aria-label="Head diagram shading a band around the head"></div><span class="face-name">Tension</span><span class="face-note">pain is like a band squeezing the head.</span></div>
    <div class="face-cell"><div class="face-art" role="img" aria-label="Head diagram shading one side of the head"></div><span class="face-name">Migraine</span><span class="face-note">pain, nausea and visual changes are typical of classic form.</span></div>
    <div class="face-cell"><div class="face-art" role="img" aria-label="Head diagram shading top and back of head"></div><span class="face-name">Neck</span><span class="face-note">pain is at the top and/or back of head.</span></div>
  </div>

  <div style="left:314px;top:352px">
    <div class="mini-title" style="width:60px">CLICK/ POP</div>
    <div class="option-grid">
      <span class="option"><span class="box"></span>Increased</span><span class="option"><span class="box"></span>Decreased</span>
      <span class="option"><span class="box"></span>No Change</span>
    </div>
    <div class="mini-title" style="width:89px">OPENING ABILITY</div>
    <div class="option-grid">
      <span class="option"><span class="box"></span>Increased</span><span class="option"><span class="box"></span>Decreased</span>
      <span class="option"><span class="box"></span>No Change</span>
    </div>
  </div>

  <h2 class="section-title" style="top:455px">TRIGGERS (CHECK ALL THAT APPLY)</h2>
  <div class="trigger-grid">
    <span class="option"><span class="box"></span>Sleep</span>
    <span class="option"><span class="box"></span>Insomnia</span>
    <span class="option"><span class="box"></span>Yawn</span>
    <span class="option"><span class="box"></span>Stress at Work</span>
    <span class="option"><span class="box"></span>My First Thing in AM</span>
    <span class="option"><span class="box"></span>Eating</span>
    <span class="option"><span class="box"></span>PMS/ Menstration</span>
    <span class="option"><span class="box"></span>Weather</span>
    <span class="option"><span class="box"></span>Clenching</span>
    <span class="option"><span class="box"></span>Work</span>
    <span class="option"><span class="box"></span>Stress at Home</span>
    <span class="option"><span class="box"></span>Other</span>
  </div>

  <div class="state-line" style="left:22px;top:537px;width:225px">
    <span class="label">MY SAWS WAS</span>
    <span class="option small"><span class="box small"></span>Clenched</span>
    <span class="option small"><span class="box small"></span>Relaxed</span>
  </div>
  <div class="state-line" style="left:292px;top:537px;width:192px">
    <span class="label">MY BREATH WAS</span>
    <span class="option small"><span class="box small"></span>Clenched</span>
  </div>
  <div class="state-line" style="left:22px;top:560px;width:462px">
    <span class="label">MY NECK/ SHOULDERS WERE</span>
    <span class="option small"><span class="box small"></span>Clenched</span>
    <span class="option small"><span class="box small"></span>Relaxed</span>
  </div>

  <h2 class="section-title" style="top:594px">RELIEF MEASURES (CHECK ALL THAT APPLY)</h2>
  <div class="relief-grid">
    <span class="option"><span class="box"></span>Deep Breathing</span>
    <span class="option"><span class="box"></span>Heat/ Cold</span>
    <span class="option"><span class="box"></span>Gentle Stretching</span>
    <span class="option"><span class="box"></span>Teeth apart/ Relax jaw</span>
    <span class="option"><span class="box"></span>Medication</span>
    <span class="option"><span class="box"></span>Posture Correction</span>
    <span class="option"><span class="box"></span>Self Massage</span>
    <span class="option"><span class="box"></span>Rest</span>
    <span class="option"><span class="box"></span>Mindful Reset</span>
    <span class="option"><span class="box"></span>Stabilization Exercise</span>
    <span class="option"><span class="box"></span>Others</span>
  </div>
  <div class="others-line" style="top:678px;left:285px;width:203px"></div>

  <h2 class="section-title" style="top:-1000px"></h2>
</main>
<style>
  .journal-page { overflow: hidden; }
  .journal-page .relief-grid { top: 613px; }
</style>
</body>
</html>
```